pathology learning flashcard template graphic design .

Creative designs for 2 sides of the flashcards to include colorful sectioning and font sizes that will make it easy to use in studying.

```html
<!DOCTYPE html>
<html lang="en">
<head>
<meta charset="UTF-8">
<title>Achalasia Flashcard</title>
<link rel="stylesheet" href="https://fonts.googleapis.com/css2?family=Comic+Neue:ital,wght@0,400;0,700;1,700&display=swap">
<style>
  :root {
    --bg-top: #bfeaf5;
    --bg-mid: #d9f3f9;
    --bg-bottom: #eefafd;
    --navy: #0d4a74;
    --label-blue: #1d5e8c;
    --ink: #1a1a1a;
    --white: #ffffff;
    --organ-pink: rgba(232, 150, 150, 0.28);
    --organ-blue: rgba(140, 200, 230, 0.35);
  }
  * { margin: 0; padding: 0; box-sizing: border-box; }
  html, body { width: 720px; height: 1200px; overflow: hidden; }
  body {
    position: relative;
    font-family: "Comic Neue", "Comic Sans MS", sans-serif;
    color: var(--ink);
    background: linear-gradient(180deg, var(--bg-top) 0%, var(--bg-mid) 45%, var(--bg-bottom) 100%);
  }
  .organ-art {
    position: absolute;
    left: 262px;
    top: 200px;
    width: 430px;
    height: 960px;
    border-radius: 40% 45% 50% 40% / 30% 35% 45% 40%;
    background: radial-gradient(ellipse at 60% 40%, var(--organ-blue) 0%, var(--organ-pink) 55%, rgba(255,255,255,0) 80%);
  }
  .card-title {
    position: absolute;
    top: 72px;
    left: 0;
    width: 720px;
    text-align: center;
    font-size: 52px;
    font-weight: 700;
    letter-spacing: 2px;
    color: var(--navy);
  }
  .section-label {
    position: absolute;
    left: 24px;
    font-size: 28px;
    font-weight: 700;
    color: var(--label-blue);
  }
  .section-body {
    position: absolute;
    left: 24px;
    width: 684px;
    font-size: 22px;
    line-height: 34.5px;
    color: var(--ink);
  }
  .label-definition { top: 186px; }
  .body-definition { top: 230px; }
  .label-symptoms { top: 338px; }
  .body-symptoms { top: 381px; }
  .answer-banner {
    position: absolute;
    left: 0;
    top: 552px;
    width: 308px;
    height: 54px;
    background: var(--navy);
    clip-path: polygon(0 0, 100% 0, 94% 100%, 0 100%);
  }
  .answer-banner span {
    position: absolute;
    left: 24px;
    top: 6px;
    font-size: 36px;
    font-weight: 700;
    font-style: italic;
    letter-spacing: 1px;
    color: var(--white);
  }
  .answer-text {
    position: absolute;
    left: 24px;
    top: 644px;
    width: 670px;
    font-size: 26px;
    line-height: 36.6px;
    letter-spacing: 1.2px;
    text-align: justify;
    color: var(--ink);
  }
</style>
</head>
<body>
  <div class="organ-art" role="img" aria-label="Faint illustration of the esophagus and stomach"></div>

  <h1 class="card-title">ACHALASIA</h1>

  <h2 class="section-label label-definition">Definition:</h2>
  <p class="section-body body-definition">•Motility disorder where esophageal relaxation is impaired in the lower esophageal sphincter (LES).</p>

  <h2 class="section-label label-symptoms">P/E and Symptoms:</h2>
  <p class="section-body body-symptoms">•Dysphagia that is progressive, regurgitation, weight-loss, dry cough, chest pain, GERD, esophageal perforation, squamous cell carcinoma, aspiration pneumonia.</p>

  <div class="answer-banner"><span>C - Achalasia</span></div>

  <p class="answer-text">Symptoms and studies suggestive of achalasia. Patient’s manometry presents with no relaxation of the lower esophageal sphincter during swallowing. Patient also complains of dysphagia and is unable to swallow properly, leading to weight loss. Patient has no past infection or inflammation, ruling out eosinophilic esophagitis. Patient does not have chronic GERD, eliminating the possibility of Barrett esophagus, in which at least 5 years of acid reflux are beforehand to develop columnar metaplasia.</p>
</body>
</html>
```